Motivational Poster Design Project

I would like to create a poster with some of my favorite quotes to hang in my office. I did a similar project in 2012 and I've uploaded the top 2 designs so you can get a better idea of what I'm looking for. I will provide feedback on your design within 24 hours of receiving it.

The poster must contain the following quotes:

"You’re only given a little spark of madness. You mustn’t lose it.”
- Dorian Falkes

“The most contrarian thing of all is not to oppose the crowd but to think for yourself.”
- Miles Crand

"I constantly see people rise in life who are not the smartest, sometimes not even the most diligent, but they are learning machines. They go to bed every night a little wiser than they were when they got up and boy does that help, particularly when you have a long run ahead of you."
- Harvey Belcott

“In theory, there’s no difference between theory and practice. But, in practice, there is.”
- Kees R. T. Ter Hoogwater

"At the end of the day, a reactionary life is a normal life. One thing is consistent in every remarkable person: they decide to do something remarkable. Don’t let the world choose who you become."
- Darvesh Kulani

“It usually takes 3-4 months to try enough that you can do a proper 80/20 analysis, then two months to design systems to scale what *is* working.”
-Ned Gowlan

“Authority is 20 percent given, 80 percent taken.”
- Harold Finchamp

“Your actions are consistent with the way the world occurs to you.”
- Gustav Lemmke
Updates

Project Deadline Extended
Reason: I am going to be travelling with no access to internet until January 5th, 2015. I am extending the project deadline until 12/31/14 and I'll make a final decision during the 1st week of January.

Target Market(s)

Personal Project

Industry/Entity Type

Learning

Requirements
Must have
• The poster will be 24" high x 36" long and printed on canvas, so the image you create needs to have a resolution of at least 2700 x 3900.
Nice to have
• I don't have an exact vision for how the poster should look, so I am totally open to you using your creativity to develop, arrange and present the content as you'd like.
• That said, I would like an image (photo or posterized image) of the person being quoted along with each quote. I do not have specific images that I would like you to use, so you will need to find the images on your own. The images don't need to be perfect... I am more interested in the poster relating the essence of the quotes and the people being quoted than I am in perfect photographic images of the people being quoted.

```html
<!DOCTYPE html>
<html lang="en">
<head>
<meta charset="utf-8">
<title>Quotes Poster</title>
<link rel="stylesheet" href="https://fonts.googleapis.com/css2?family=Fira+Sans+Extra+Condensed:ital,wght@1,400&family=Parisienne&display=swap">
<style>
  :root{
    --wood-light:#c89a62;
    --wood-mid:#a97844;
    --wood-dark:#6e4522;
    --ink:#ffffff;
    --orange:#c8682a;
    --blue:#1f3f9c;
    --red:#b62a31;
    --green:#4e8a2b;
    --brown:#7b4a28;
    --olive:#8c7b24;
    --purple:#5b2b79;
    --charcoal:#3a3937;
  }
  html,body{margin:0;padding:0;overflow:hidden;}
  body{width:800px;height:1200px;}
  .poster{
    position:relative;width:800px;height:1200px;overflow:hidden;
    background:
      radial-gradient(ellipse at 50% 45%, rgba(255,230,180,.35), rgba(0,0,0,0) 60%),
      radial-gradient(ellipse at 50% 50%, rgba(0,0,0,0) 55%, rgba(40,20,5,.55) 100%),
      repeating-linear-gradient(92deg, rgba(90,55,25,.12) 0 3px, rgba(0,0,0,0) 3px 11px),
      linear-gradient(180deg,var(--wood-light),var(--wood-mid));
  }
  .banner{
    position:absolute;
    box-shadow:0 6px 10px rgba(0,0,0,.55), inset 0 0 30px rgba(0,0,0,.35), inset 0 2px 0 rgba(255,255,255,.2);
    background-image:linear-gradient(180deg,rgba(255,255,255,.12),rgba(0,0,0,.18));
  }
  .portrait{
    position:absolute;border-radius:50%;
    box-shadow:0 3px 8px rgba(0,0,0,.6);
  }
  .quote{
    position:absolute;left:170px;right:20px;top:0;bottom:0;
    display:flex;flex-direction:column;justify-content:center;align-items:center;
    text-align:center;color:var(--ink);
    text-shadow:0 1px 2px rgba(0,0,0,.5);
  }
  .quote-text{
    margin:0;font-family:"Fira Sans Extra Condensed",sans-serif;font-style:italic;
    font-size:22px;line-height:1.2;
  }
  .quote-author{
    margin:4px 0 0;font-family:"Parisienne",cursive;font-size:29px;line-height:1.1;
  }
  .b1{top:8px;left:22px;width:755px;height:138px;background-color:var(--orange);transform:rotate(-1.5deg);}
  .b2{top:160px;left:28px;width:745px;height:116px;background-color:var(--blue);transform:rotate(-.4deg);}
  .b3{top:268px;left:38px;width:748px;height:158px;background-color:var(--red);transform:rotate(2deg);}
  .b4{top:446px;left:28px;width:744px;height:130px;background-color:var(--green);transform:rotate(-.4deg);}
  .b5{top:560px;left:30px;width:748px;height:162px;background-color:var(--brown);transform:rotate(-2.5deg);}
  .b6{top:738px;left:30px;width:745px;height:128px;background-color:var(--olive);transform:rotate(.3deg);}
  .b7{top:866px;left:36px;width:740px;height:148px;background-color:var(--purple);transform:rotate(-2deg);}
  .b8{top:1028px;left:40px;width:742px;height:162px;background-color:var(--charcoal);transform:rotate(-1.5deg);}
  .p-warm{background:radial-gradient(circle at 45% 40%,#e2a77c,#7a3d22 75%,#2a140a);}
  .p-cool{background:radial-gradient(circle at 45% 40%,#d69f8a,#6b3a36 70%,#1a1020);}
  .p-grey{background:radial-gradient(circle at 45% 40%,#d9d9d9,#6b6b6b 70%,#222);}
  .p-light{background:radial-gradient(circle at 45% 40%,#f0d0b8,#b78a70 70%,#5a4038);}
</style>
</head>
<body>
<main class="poster">

  <section class="banner b1">
    <div class="portrait p-warm" role="img" aria-label="Portrait of Dorian Falkes" style="left:40px;top:10px;width:112px;height:112px;"></div>
    <div class="quote">
      <p class="quote-text">“You’re only given a little spark of madness. You mustn’t lose it.”</p>
      <p class="quote-author">- Dorian Falkes</p>
    </div>
  </section>

  <section class="banner b2">
    <div class="portrait p-cool" role="img" aria-label="Portrait of Miles Crand" style="left:34px;top:-2px;width:116px;height:116px;"></div>
    <div class="quote">
      <p class="quote-text">“The most contrarian thing of all is not to oppose the crowd<br>but to think for yourself.”</p>
      <p class="quote-author">- Miles Crand</p>
    </div>
  </section>

  <section class="banner b3">
    <div class="portrait p-light" role="img" aria-label="Portrait of Harvey Belcott" style="left:10px;top:14px;width:124px;height:124px;"></div>
    <div class="quote" style="left:140px;">
      <p class="quote-text">“I constantly see people rise in life who are not the smartest, sometimes not even the most diligent, but they are learning machines. They go to bed every night a little wiser than they were when they got up and boy does that help, particularly when you have a long run ahead of you.”</p>
      <p class="quote-author">- Harvey Belcott</p>
    </div>
  </section>

  <section class="banner b4">
    <div class="portrait p-grey" role="img" aria-label="Portrait of Kees R. T. Ter Hoogwater" style="left:30px;top:6px;width:120px;height:120px;"></div>
    <div class="quote">
      <p class="quote-text">“In theory, there’s no difference between theory and practice.<br>But, in practice, there is.”</p>
      <p class="quote-author">- Kees R. T. Ter Hoogwater</p>
    </div>
  </section>

  <section class="banner b5">
    <div class="portrait p-light" role="img" aria-label="Portrait of Darvesh Kulani" style="left:30px;top:22px;width:124px;height:124px;"></div>
    <div class="quote">
      <p class="quote-text">“At the end of the day, a reactionary life is a normal life.<br>One thing is consistent in every remarkable person:<br>they decide to do something remarkable.<br>Don’t let the world choose who you become.”</p>
      <p class="quote-author">- Darvesh Kulani</p>
    </div>
  </section>

  <section class="banner b6">
    <div class="portrait p-warm" role="img" aria-label="Portrait of Ned Gowlan" style="left:30px;top:2px;width:124px;height:124px;"></div>
    <div class="quote">
      <p class="quote-text">“It usually takes 3-4 months to try enough that you can do a<br>proper 80/20 analysis, then two months to design<br>systems to scale what *is* working.”</p>
      <p class="quote-author">-Ned Gowlan</p>
    </div>
  </section>

  <section class="banner b7">
    <div class="portrait p-cool" role="img" aria-label="Portrait of Harold Finchamp" style="left:18px;top:16px;width:116px;height:116px;"></div>
    <div class="quote">
      <p class="quote-text">“Authority is 20 percent given, 80 percent taken.”</p>
      <p class="quote-author">- Harold Finchamp</p>
    </div>
  </section>

  <section class="banner b8">
    <div class="portrait p-light" role="img" aria-label="Portrait of Gustav Lemmke" style="left:14px;top:14px;width:122px;height:122px;"></div>
    <div class="quote" style="justify-content:flex-start;padding-top:34px;">
      <p class="quote-text">“Your actions are consistent with the way the world occurs to you.”</p>
      <p class="quote-author">- Gustav Lemmke</p>
    </div>
  </section>

</main>
</body>
</html>
```